Wordpress Design Project (Brannock)

We need a wordpress design for an established auction and real estate company based in Minnesota. The winning design will incorporate the colors of logo (red white and black) creatively in a very professional and clean layout. Client mentions liking the site http://www.quillbrook.example/ and http://www.tarvenlodeauction.example/ as a general idea for what they like.

Industry/Entity Type

Real Estate

Requirements
Must have
• Navigation:
1) Home - will have auction list, no text
2) Upcoming Auctions
3) Online Auctions
4) Real Estate
5) Auction Gallery
6) For Sale
7) About Us
8) Contact Us

Sidebar widget will include:
- email signup
- asset for sale fader (seen in Featured Listings at http://www.tarvenlodeauction.example/)
- Slideshow - initial image attached
- Video widget (image attached)
- social media icons for Vidlark, Friendspan, Chirpel, Workloop and RSS feed
- testimonials

Footer will have smaller logo and contact info
Nice to have
• Nice to Have:
- use of drop-down menu design for 'About Us'
1) About Brannock
2) Testimonials

```html
<!DOCTYPE html>
<html lang="en">
<head>
<meta charset="utf-8">
<title>Brannock Auction &amp; Real Estate Services</title>
<link href="https://fonts.googleapis.com/css2?family=Roboto+Condensed:ital,wght@0,400;0,700;1,400&family=Open+Sans:ital,wght@0,400;0,600;1,400;1,600&display=swap" rel="stylesheet">
<style>
:root{
  --red:#d4161c;
  --red-dark:#a50f14;
  --ink:#1e1e1e;
  --panel:#2b2b2b;
  --grey:#d9d9d9;
  --text:#6b6b6b;
  --white:#fff;
  --gold:#f4c542;
}
*{margin:0;padding:0;box-sizing:border-box}
html,body{width:840px;height:1200px;overflow:hidden}
body{position:relative;background:var(--white);font-family:"Open Sans",sans-serif;color:var(--text)}
.cond{font-family:"Roboto Condensed",sans-serif}
.backdrop{position:absolute;left:0;top:331px;width:840px;height:869px;background:linear-gradient(#cfcfcf,#ececec 45%,#f4f4f4)}
.nav{position:absolute;left:144px;top:0;display:flex;height:68px}
.nav a{font-family:"Roboto Condensed",sans-serif;font-size:13px;color:var(--red);text-decoration:none;padding:40px 12px 0;}
.nav a.active{background:linear-gradient(var(--red),#b01116);color:var(--white);font-weight:700;width:44px;padding:40px 0 0;text-align:center}
.logo{position:absolute;left:24px;top:88px;width:138px;height:66px;display:flex;align-items:center;gap:7px}
.logo .mark{width:16px;height:16px;background:var(--red)}
.logo span{font-family:"Roboto Condensed",sans-serif;font-weight:700;font-size:25px;color:var(--red)}
.btns{position:absolute;left:25px;top:182px;display:flex;gap:14px}
.btn{width:64px;height:31px;border-radius:6px;background:linear-gradient(#fff,#e3e3e3);border-left:5px solid var(--red);border-right:5px solid var(--red);font-family:"Roboto Condensed",sans-serif;font-size:14px;text-align:center;line-height:31px;color:var(--ink);box-shadow:0 1px 3px rgba(0,0,0,.3)}
.btn.reg{width:80px;color:var(--red)}
.social{position:absolute;left:25px;top:233px;display:flex;gap:5px}
.social span{width:24px;height:24px;border-radius:50%;background:#8a8a8a;border:2px solid #d0d0d0}
.testimonial{position:absolute;left:25px;top:291px;width:163px;height:221px;background:var(--panel);padding:10px 14px}
.testimonial h3{font-family:"Roboto Condensed",sans-serif;font-weight:700;font-size:20px;color:var(--gold);display:flex;align-items:center;gap:8px}
.testimonial h3 i{width:22px;height:18px;border-radius:50%;background:#e98a1e;display:block}
.testimonial h4{font-family:"Roboto Condensed",sans-serif;font-style:italic;font-weight:700;font-size:12px;color:#fff;margin:20px 0 10px 4px}
.testimonial p{font-size:10px;line-height:18px;color:#aaa;margin-left:4px}
.testimonial .corner{position:absolute;right:0;bottom:0}
.hero{position:absolute;left:188px;top:68px;width:628px;height:444px;background:linear-gradient(160deg,#6a6a5a,#4b7d3a 35%,#5a5046 60%,#3a6a2e)}
.thumbs{position:absolute;left:347px;top:470px;display:flex;gap:2px}
.thumbs div{width:156px;height:42px;background:linear-gradient(#8a9a8a,#5c6a52)}
.featured{position:absolute;left:33px;top:512px;width:774px;height:261px;background:var(--white)}
.featured h2{position:absolute;left:17px;top:12px;font-family:"Roboto Condensed",sans-serif;font-weight:700;font-size:20px;color:var(--red)}
.featured .seeall{position:absolute;right:12px;top:18px;font-family:"Roboto Condensed",sans-serif;font-size:12px;color:var(--ink)}
.lead{position:absolute;left:2px;top:50px;width:193px;height:211px;background:var(--red);border-top:5px solid var(--ink);padding:22px 14px 0}
.lead h3{font-family:"Roboto Condensed",sans-serif;font-size:19px;color:#fff;font-weight:400;margin-left:4px}
.lead p{font-size:10px;font-style:italic;font-weight:600;line-height:19.5px;color:#fff;margin-top:8px}
.lead .tools{position:absolute;right:0;bottom:0;display:flex;gap:3px}
.lead .tools div{width:34px;height:29px;background:var(--ink);display:flex;align-items:center;justify-content:center}
.card{position:absolute;top:50px;width:191px;height:211px;background:#e2e2e2;border-bottom:3px solid var(--red)}
.card .photo{height:155px;background:linear-gradient(#5b6a74,#6a5a4a 50%,#3f6a34)}
.card p{text-align:center;font-family:"Roboto Condensed",sans-serif;font-size:17px;color:var(--red);margin-top:18px;font-weight:700}
.welcome{position:absolute;left:17px;top:799px;width:806px;height:177px;background:#fafafa;box-shadow:0 6px 8px -4px rgba(0,0,0,.25)}
.welcome h2{position:absolute;left:12px;top:14px;font-family:"Roboto Condensed",sans-serif;font-weight:700;font-size:20px;color:var(--red-dark)}
.welcome .dots{position:absolute;left:12px;top:44px;width:546px;border-top:3px dotted #ddd}
.welcome p{position:absolute;left:11px;top:56px;width:550px;font-size:10.5px;line-height:17.8px;text-align:justify}
.welcome .more{position:absolute;left:494px;top:157px;font-size:9px;font-style:italic;font-weight:600;color:var(--red-dark)}
.video{position:absolute;left:571px;top:0;width:235px;height:177px;background:#111}
.video .title{position:absolute;left:10px;top:10px;font-family:"Roboto Condensed",sans-serif;font-size:11px;color:#fff;font-weight:700}
.video .screen{position:absolute;left:0;top:27px;width:235px;height:135px;background:linear-gradient(#e9e3e3,#c8a9a9 60%,#e3e3e3)}
.footer{position:absolute;left:17px;top:1010px;width:807px;height:190px;background:var(--ink)}
.contact{position:absolute;left:16px;top:16px;width:775px;height:142px;background:var(--red);color:#fff}
.contact h2{position:absolute;left:15px;top:12px;font-family:"Roboto Condensed",sans-serif;font-weight:700;font-size:22px}
.contact .addr{position:absolute;left:15px;top:54px;font-size:9.5px;line-height:18px}
.contact .lines{position:absolute;left:313px;top:46px;width:182px;font-size:9.5px}
.contact .lines div{display:flex;justify-content:space-between;height:20.5px;align-items:center;border-bottom:1px solid rgba(255,255,255,.25)}
.contact .lines div:last-child{border:0}
.contact .flogo{position:absolute;left:600px;top:50px;display:flex;align-items:center;gap:8px}
.contact .flogo i{width:16px;height:16px;background:var(--red-dark);display:block}
.contact .flogo span{font-family:"Roboto Condensed",sans-serif;font-weight:700;font-size:30px;color:var(--red-dark)}
.bottom{position:absolute;left:24px;top:169px;width:775px;display:flex;justify-content:space-between;font-size:8.5px;color:#888}
.bottom nav span{margin-right:6px}
.bottom nav span+span:before{content:"/";margin-right:6px;color:#555}
</style>
</head>
<body>
<div class="backdrop"></div>

<nav class="nav">
  <a class="active">Home</a><a>About Us</a><a>Upcoming Auctions</a><a>Online Auctions</a><a>Real Estate</a><a>Auction Gallery</a><a>For Sale</a><a>Contact Us</a>
</nav>

<div class="logo"><div class="mark"></div><span>Brannock</span></div>
<div class="btns"><div class="btn">Login</div><div class="btn reg">Register</div></div>
<div class="social" aria-label="Friendspan, Chirpel, Workloop, Vidlark, RSS"><span></span><span></span><span></span><span></span><span></span></div>

<section class="testimonial">
  <h3><i></i>Testimonial</h3>
  <h4>Harlow, MN</h4>
  <p>Lorem ipsum dolor met, consectetur adipiscing elit. Donec mauris mi, mattis ac Lorem ipsum dolor sit amet, consectetur adipiscing elit. Donec</p>
  <svg class="corner" width="30" height="30"><path d="M30 0V30H0Z" fill="#d4161c"/><circle cx="21" cy="21" r="3.5" fill="none" stroke="#fff" stroke-width="1.3"/></svg>
</section>

<div class="hero" role="img" aria-label="Large crowd of bidders among green farm tractors at an outdoor auction"></div>
<div class="thumbs"><div role="img" aria-label="Loaders in snow"></div><div role="img" aria-label="Auction crowd"></div><div role="img" aria-label="Trailers"></div></div>

<section class="featured">
  <h2>Featured Listings:</h2>
  <div class="seeall">See all ▸</div>
  <div class="lead">
    <h3>Real Estate For Sale</h3>
    <p>Lorem ipsum dolor sit amet, con-sectetur adipiscing elit. spendisse tincidunt interd llicitudin. Nullam quis lacus enim. Curatur nec dolor tellus, non eleifend mauris.</p>
    <div class="tools">
      <div><svg width="16" height="16"><circle cx="6.5" cy="6.5" r="4.5" fill="none" stroke="#fff" stroke-width="2"/><path d="M10 10l4.5 4.5" stroke="#fff" stroke-width="2.5"/></svg></div>
      <div><svg width="16" height="16"><path d="M6 10l4-4M4 9l-1.5 1.5a2.5 2.5 0 003.5 3.5L7.5 12.5M12 7l1.5-1.5a2.5 2.5 0 00-3.5-3.5L8.5 3.5" stroke="#fff" stroke-width="2" fill="none"/></svg></div>
    </div>
  </div>
  <div class="card" style="left:196px"><div class="photo" role="img" aria-label="Auction crowd around equipment"></div><p>Lorem ipsum</p></div>
  <div class="card" style="left:389px"><div class="photo" role="img" aria-label="Auction crowd around equipment"></div><p>Lorem ipsum</p></div>
  <div class="card" style="left:582px"><div class="photo" role="img" aria-label="Auction crowd around equipment"></div><p>Lorem ipsum</p></div>
</section>

<section class="welcome">
  <h2>Welcome to out site!</h2>
  <div class="dots"></div>
  <p>Lorem ipsum dolor sit amet, consectetur adipiscing elit. Donec mauris mi, mattis ac condimentum ullamcorper, consectetur eu lectus. Duis congue varius lacus, cursus luctus magna dignissim sit amet. Integer cursus sed mauris a convallis. Cras scelerisque arcu purus, at tempor quam congue id. Donec luctus risus eu enim vulputate suscipit. Nam gravida ac libero non viverra. Pellentesque quam lorem, ullamcorper sit amet pellentesque ut, pellentesque nec nisi. Nullam mollis nunc porta ligula rhoncus, ac lacinia lorem</p>
  <div class="more">Read more...</div>
  <div class="video">
    <div class="title">Brannock Bidder Tutorial.mp4</div>
    <div class="screen" role="img" aria-label="Video still of the online bidding screen"></div>
    <svg style="position:absolute;left:98px;top:75px" width="40" height="40"><circle cx="20" cy="20" r="18" fill="rgba(255,255,255,.35)" stroke="#fff" stroke-width="2"/><path d="M16 12l11 8-11 8z" fill="#fff"/></svg>
  </div>
</section>

<footer class="footer">
  <div class="contact">
    <h2>Contact Us</h2>
    <div class="addr">48 Elm Street West Harlow, MN 56999<br>Dale Brannock, Auctioneer, MN Lic. 7000412<br>Reed Halvorsen, Auctioneer, MN Lic. 21-88<br>Owen Tessmer, Online Auction Coordinator</div>
    <div class="lines">
      <div><span>✉ Mail:</span><span>info@brannockauctions.example</span></div>
      <div><span>☎ Office:</span><span>320-555-0143</span></div>
      <div><span>✆ Cell:</span><span>320-555-0172</span></div>
      <div><span>▤ Fax:</span><span>320-555-0198</span></div>
    </div>
    <div class="flogo"><i></i><span>Brannock</span></div>
  </div>
  <div class="bottom">
    <nav><span>Home</span><span>About Us</span><span>Upcoming Auctions</span><span>Online Auctions</span><span>Real Estate</span><span>Auction Gallery</span><span>For Sale</span><span>Contact Us</span></nav>
    <div>(c)2013 Brannock. All rights reserved</div>
  </div>
</footer>
</body>
</html>
```